Clean and modern business cards

Looking for an updated business card design for my dental office “tovrelle dental” . Looking for a modern clean / sleek design . I’m thinking black background but open to seeing other options . One side needs to have an appointment card . Card needs to have logo, dentist name , phone, email , address . I’ve attached couple of cards I thought were cool as well as my logo
Target Market(s)
Dental patients
Industry/Entity Type
Dentistry
Contact Information for Business Card
Phone email address

```html
<!DOCTYPE html>
<html lang="en">
<head>
<meta charset="utf-8">
<title>Tovrelle Dental – Business Card</title>
<link href="https://fonts.googleapis.com/css2?family=Montserrat:wght@300;400;600;700;800&display=swap" rel="stylesheet">
<style>
  :root {
    --page: #f2f2f2;
    --card: #ffffff;
    --ink: #111111;
    --accent: #8cc63f;
  }
  * { box-sizing: border-box; margin: 0; padding: 0; }
  html, body { width: 1200px; height: 900px; overflow: hidden; }
  body {
    position: relative;
    background: var(--page);
    font-family: "Montserrat", sans-serif;
    color: var(--ink);
  }
  .card {
    position: absolute;
    left: 285px;
    width: 630px;
    height: 360px;
    background: var(--card);
  }
  .card-front { top: 63px; }
  .card-back { top: 478px; }

  .brand {
    position: absolute;
    display: flex;
    align-items: center;
    justify-content: center;
    gap: 10px;
    font-family: "Montserrat", sans-serif;
    font-weight: 700;
    color: var(--ink);
    text-transform: uppercase;
    white-space: nowrap;
  }
  .brand-dot {
    border-radius: 50%;
    background: var(--accent);
    flex: none;
  }
  .brand-front {
    left: 0; right: 0; top: 160px;
    font-size: 30px;
    letter-spacing: 3px;
  }
  .brand-front .brand-dot { width: 22px; height: 22px; }
  .brand-back {
    left: 470px; top: 70px; width: 150px;
    font-size: 13px;
    letter-spacing: 1px;
    gap: 6px;
  }
  .brand-back .brand-dot { width: 10px; height: 10px; }

  .appointment-title {
    position: absolute;
    left: 26px; top: 80px;
    font-size: 22px;
    font-weight: 300;
  }
  .blank {
    position: absolute;
    left: 30px;
    width: 125px;
    border-top: 2px dotted var(--ink);
    text-align: center;
    font-size: 13px;
    font-weight: 400;
    padding-top: 2px;
  }
  .blank-date { top: 145px; }
  .blank-time { top: 201px; }
  .cancel-note {
    position: absolute;
    left: 20px; top: 251px; width: 290px;
    text-align: center;
    font-size: 11.2px;
    font-weight: 700;
    line-height: 14px;
  }
  .divider {
    position: absolute;
    left: 315px; top: 145px;
    width: 2px; height: 184px;
    background: var(--ink);
  }
  .contact-list { list-style: none; }
  .contact-item {
    position: absolute;
    left: 321px;
    display: flex;
    align-items: center;
    gap: 10px;
    font-size: 13px;
    font-weight: 400;
    white-space: nowrap;
  }
  .icon {
    width: 22px; height: 22px;
    border: 2px solid var(--accent);
    display: flex; align-items: center; justify-content: center;
    flex: none;
  }
  .icon svg { width: 12px; height: 12px; fill: var(--accent); }
  .contact-name { top: 152px; font-size: 20px; font-weight: 800; gap: 6px; }
  .contact-name .icon { width: 27px; height: 27px; }
  .contact-name .icon svg { width: 15px; height: 15px; }
  .contact-address { top: 195px; }
  .contact-phone { top: 230px; }
  .contact-web { top: 265px; }
  .contact-email { top: 301px; }
</style>
</head>
<body>

<section class="card card-front">
  <div class="brand brand-front"><span class="brand-dot"></span>Tovrelle Dental</div>
</section>

<section class="card card-back">
  <div class="brand brand-back"><span class="brand-dot"></span>Tovrelle Dental</div>

  <h2 class="appointment-title">Your next appointment is:</h2>
  <div class="blank blank-date">Date</div>
  <div class="blank blank-time">Time</div>
  <p class="cancel-note">To cancel or reschedule please notify us at least 48 hours prior to your scheduled appoitment</p>

  <div class="divider"></div>

  <ul class="contact-list">
    <li class="contact-item contact-name">
      <span class="icon"><svg viewBox="0 0 12 12"><circle cx="6" cy="3.2" r="2.6"/><path d="M0.5 12c0-3.4 2.4-5.4 5.5-5.4s5.5 2 5.5 5.4z"/></svg></span>
      DR.LENORA VASQUEL
    </li>
    <li class="contact-item contact-address">
      <span class="icon"><svg viewBox="0 0 12 12"><path d="M6 0.5a4 4 0 0 0-4 4c0 3 4 7 4 7s4-4 4-7a4 4 0 0 0-4-4zm0 5.5a1.5 1.5 0 1 1 0-3 1.5 1.5 0 0 1 0 3z"/></svg></span>
      2210 FERNHILL AVE , WINNIPEG , MB
    </li>
    <li class="contact-item contact-phone">
      <span class="icon"><svg viewBox="0 0 12 12"><path d="M2.4 0.8l2 2.2-1 1.4c0.8 1.6 2 2.8 3.6 3.6l1.4-1 2.2 2-1.2 2.2C5 11 1 7 0.8 2z"/></svg></span>
      (204) 555 - 0147
    </li>
    <li class="contact-item contact-web">
      <span class="icon"><svg viewBox="0 0 12 12"><path d="M3 0.5v10l2.5-2.5 1.8 3.8 1.6-0.8-1.8-3.7h3.4z"/></svg></span>
      TOVRELLEWPG.CA
    </li>
    <li class="contact-item contact-email">
      <span class="icon"><svg viewBox="0 0 12 12"><path d="M0.5 2.5h11v7h-11z" fill="none" stroke="#8cc63f" stroke-width="1.2"/><path d="M0.5 2.5l5.5 4 5.5-4" fill="none" stroke="#8cc63f" stroke-width="1.2"/></svg></span>
      CONTACT@TOVRELLEWPG.CA
    </li>
  </ul>
</section>

</body>
</html>
```